Business Card Design

I will be finding aged care homes for those who need placement.
Assisting with all of the paperwork.
I would like Australian wattle picture on the card/ logo please
Industry/Entity Type
Business
Contact Information for Business Card
Senior Living Pathways
Marla Jensen
PH: 0438 926 153
Email: seniorlivingpathways@mailbox.example
ABN: 63 214 958 307
PO Box 3189, Kallangur QLD 4503

```html
<!DOCTYPE html>
<html lang="en">
<head>
<meta charset="UTF-8">
<title>Senior Living Pathways – Business Card</title>
<link rel="stylesheet" href="https://fonts.googleapis.com/css2?family=Audiowide&family=Lato:wght@400;700&display=swap">
<style>
  :root {
    --page-bg: #1b1b1b;
    --card-dark: #2b2b2b;
    --wattle-yellow: #d9b22a;
    --name-white: #ffffff;
    --body-text: #f2f2f2;
    --photo-green: #4f6b2a;
    --photo-yellow: #e8d01e;
  }
  * { margin: 0; padding: 0; box-sizing: border-box; }
  html, body {
    width: 1200px;
    height: 1000px;
    overflow: hidden;
    background: var(--page-bg);
  }
  .stage {
    width: 1200px;
    height: 1000px;
    display: flex;
    align-items: center;
    justify-content: center;
  }
  .business-card {
    width: 900px;
    height: 550px;
    display: flex;
    background: var(--card-dark);
    box-shadow: 0 20px 50px rgba(0,0,0,0.6);
  }
  .wattle-photo {
    width: 430px;
    height: 100%;
    background:
      radial-gradient(ellipse at 55% 45%, var(--photo-yellow) 0%, #c9b21c 35%, transparent 70%),
      linear-gradient(160deg, var(--photo-green) 0%, #8a9a25 45%, #6e7f26 100%);
  }
  .card-details {
    flex: 1;
    display: flex;
    flex-direction: column;
    align-items: center;
    text-align: center;
    padding-top: 78px;
  }
  .business-name {
    font-family: "Audiowide", sans-serif;
    color: var(--wattle-yellow);
    font-size: 40px;
    line-height: 1.2;
    letter-spacing: 1px;
    text-transform: uppercase;
  }
  .person-name {
    font-family: "Audiowide", sans-serif;
    color: var(--name-white);
    font-size: 32px;
    margin-top: 46px;
    text-transform: uppercase;
  }
  .contact-list {
    list-style: none;
    margin-top: 50px;
    font-family: "Lato", sans-serif;
    font-size: 19px;
    color: var(--body-text);
    line-height: 1.75;
  }
  .contact-label {
    color: var(--wattle-yellow);
    font-weight: 700;
  }
  .abn-line {
    margin-top: 26px;
    font-family: "Lato", sans-serif;
    font-size: 19px;
    color: var(--body-text);
  }
</style>
</head>
<body>
  <main class="stage">
    <article class="business-card">
      <div class="wattle-photo" role="img" aria-label="Photograph of Australian golden wattle blossoms with green foliage"></div>
      <section class="card-details">
        <h1 class="business-name">Senior Living<br>Pathways</h1>
        <h2 class="person-name">Marla Jensen</h2>
        <ul class="contact-list">
          <li><span class="contact-label">P:</span> 0438 926 153</li>
          <li><span class="contact-label">E:</span> seniorlivingpathways@mailbox.example</li>
          <li><span class="contact-label">A:</span> PO Box 3189, Kallangur QLD 4503</li>
        </ul>
        <p class="abn-line"><span class="contact-label">ABN:</span> 63 214 958 307</p>
      </section>
    </article>
  </main>
</body>
</html>
```